Bramblewick Keystone

Looking for modern business cards.
Clean contemporary design.
Similar to this.
https://www.snapvorlo.net/imgview?src=https%3A%2F%2Fcdn.printquell.net%2Fprofessional_elegant_modern_black_plain_metal_business_card-a1b2c3d4e5f60718293a4b5c6d7e8f90_qwxyz_4tmpl_540.jpg&ref=https%3A%2F%2Fwww.printquell.net%2Fprofessional_elegant_modern_black_plain_metal_business_card-100200300400500600&id=7aB9cD3e-QR5TU&tid=Xyz_abc123defGH%3A&v=10abcDEFghiJKLmnoPQRstUVwxYZ0123456789abcd..x&w=540&h=540&bih=1360&biw=1061&q=modern%20business%20cards&ref2=0abcDEFghiJKLmnoPQRstUVwxYZ0123456789abcd&ia=mrc&ua=8

But I'd like the blue to look metallic.

```html
<!DOCTYPE html>
<html lang="en">
<head>
<meta charset="utf-8">
<title>Bramblewick Keystone – Business Cards</title>
<link rel="stylesheet" href="https://fonts.googleapis.com/css2?family=Arimo:wght@400;700&display=swap">
<style>
  :root {
    --backdrop: #c6e6dc;
    --ink-teal: #1aa3c6;
    --accent-red: #e3242b;
    --white: #ffffff;
    --metal-black-1: #050505;
    --metal-black-2: #2b2b2b;
    --metal-blue-dark: #0789ab;
    --metal-blue-mid: #1fb3d6;
    --metal-blue-light: #8fdcef;
    --card-radius: 34px;
  }
  * { box-sizing: border-box; }
  html, body {
    margin: 0;
    width: 1200px;
    height: 856px;
    overflow: hidden;
    background: var(--backdrop);
    font-family: "Arimo", Arial, sans-serif;
  }
  .card-sheet {
    position: relative;
    width: 1200px;
    height: 856px;
  }
  .card {
    position: absolute;
    top: 278px;
    width: 520px;
    height: 300px;
    border-radius: var(--card-radius);
    overflow: hidden;
    box-shadow: 0 14px 30px rgba(20, 60, 50, 0.22);
  }

  /* Front: brushed black metal */
  .card--front {
    left: 60px;
    background:
      repeating-linear-gradient(98deg, rgba(255,255,255,0.035) 0 1px, transparent 1px 4px, rgba(255,255,255,0.02) 4px 5px, transparent 5px 9px),
      radial-gradient(ellipse 60% 70% at 62% 38%, var(--metal-black-2), var(--metal-black-1) 75%);
  }
  .brand {
    position: absolute;
    display: flex;
    align-items: center;
    gap: 10px;
  }
  .brand__dot {
    width: 14px;
    height: 14px;
    border-radius: 50%;
    flex: none;
  }
  .brand__name {
    font-weight: 700;
    letter-spacing: 0.2px;
    white-space: nowrap;
  }
  .card--front .brand {
    left: 0;
    right: 0;
    top: 118px;
    justify-content: center;
  }
  .card--front .brand__dot { background: var(--accent-red); }
  .card--front .brand__name {
    font-size: 34px;
    color: var(--ink-teal);
  }
  .tagline {
    position: absolute;
    font-size: 8px;
    white-space: nowrap;
  }
  .card--front .tagline {
    left: 0;
    right: 0;
    top: 164px;
    text-align: center;
    color: var(--ink-teal);
  }

  /* Back: brushed metallic blue */
  .card--back {
    left: 620px;
    background:
      repeating-linear-gradient(92deg, rgba(255,255,255,0.06) 0 1px, transparent 1px 3px, rgba(0,60,90,0.05) 3px 4px, transparent 4px 7px),
      linear-gradient(120deg, var(--metal-blue-dark) 0%, var(--metal-blue-mid) 28%, var(--metal-blue-light) 46%, var(--metal-blue-mid) 60%, var(--metal-blue-dark) 100%);
  }
  .card--back .brand {
    left: 34px;
    top: 36px;
  }
  .card--back .brand__dot {
    width: 12px;
    height: 12px;
    background: var(--white);
  }
  .card--back .brand__name {
    font-size: 20px;
    color: var(--white);
  }
  .card--back .tagline {
    left: 56px;
    top: 62px;
    color: var(--white);
    font-size: 6.5px;
  }
  .holder {
    position: absolute;
    left: 34px;
    top: 104px;
  }
  .holder__name {
    margin: 0;
    font-size: 17px;
    font-weight: 700;
    color: var(--accent-red);
  }
  .holder__role {
    margin: 3px 0 0;
    font-size: 12px;
    color: var(--white);
  }
  .contact-list {
    position: absolute;
    left: 34px;
    top: 164px;
    margin: 0;
    padding: 0;
    list-style: none;
  }
  .contact-list__item {
    display: flex;
    align-items: center;
    gap: 9px;
    height: 22px;
    font-size: 12px;
    color: var(--white);
  }
  .contact-list__icon {
    width: 15px;
    height: 15px;
    flex: none;
  }
</style>
</head>
<body>
<main class="card-sheet">

  <section class="card card--front" aria-label="Business card front">
    <div class="brand">
      <span class="brand__dot"></span>
      <span class="brand__name">Bramblewick Keystone</span>
    </div>
    <p class="tagline">Strategy for growing businesses, every day</p>
  </section>

  <section class="card card--back" aria-label="Business card back">
    <div class="brand">
      <span class="brand__dot"></span>
      <span class="brand__name">Bramblewick Keystone</span>
    </div>
    <p class="tagline">Strategy for growing businesses, every day</p>

    <div class="holder">
      <p class="holder__name">Mr. Your Name</p>
      <p class="holder__role">Designation</p>
    </div>

    <ul class="contact-list">
      <li class="contact-list__item">
        <svg class="contact-list__icon" viewBox="0 0 16 16" aria-hidden="true">
          <circle cx="8" cy="8" r="8" fill="#e3242b"/>
          <path d="M8 3.4a3 3 0 0 0-3 3c0 2.2 3 5.8 3 5.8s3-3.6 3-5.8a3 3 0 0 0-3-3z" fill="#fff"/>
          <circle cx="8" cy="6.4" r="1.1" fill="#e3242b"/>
        </svg>
        <span>2090 address line1, address line2</span>
      </li>
      <li class="contact-list__item">
        <svg class="contact-list__icon" viewBox="0 0 16 16" aria-hidden="true">
          <circle cx="8" cy="8" r="8" fill="#e3242b"/>
          <path d="M5.2 4h1.6l.8 2-1 .8a5 5 0 0 0 2.6 2.6l.8-1 2 .8v1.6c0 .5-.4.8-.9.8A7 7 0 0 1 4.4 4.9c0-.5.3-.9.8-.9z" fill="#fff"/>
        </svg>
        <span>+36 30 555 014 2 77</span>
      </li>
      <li class="contact-list__item">
        <svg class="contact-list__icon" viewBox="0 0 16 16" aria-hidden="true">
          <circle cx="8" cy="8" r="8" fill="#e3242b"/>
          <rect x="3.8" y="5" width="8.4" height="6" rx="0.8" fill="#fff"/>
          <path d="M4 5.4 8 8.4l4-3" fill="none" stroke="#e3242b" stroke-width="0.9"/>
        </svg>
        <span>info@bramblewickkeystone.com</span>
      </li>
      <li class="contact-list__item">
        <svg class="contact-list__icon" viewBox="0 0 16 16" aria-hidden="true">
          <circle cx="8" cy="8" r="8" fill="#e3242b"/>
          <circle cx="8" cy="8" r="4.2" fill="none" stroke="#fff" stroke-width="1"/>
          <ellipse cx="8" cy="8" rx="1.8" ry="4.2" fill="none" stroke="#fff" stroke-width="0.9"/>
          <path d="M3.8 8h8.4" stroke="#fff" stroke-width="0.9"/>
        </svg>
        <span>www.bramblewickkeystone.com</span>
      </li>
    </ul>
  </section>

</main>
</body>
</html>
```